cover design for presentation folder

I am looking for a simple cover design for a 9X12 folder cover. I want our logo featured and some design element from our logo incorporated. I have attached two versions on our logo.

Colors

Designer to choose colors to be used in the design.

```html
<!DOCTYPE html>
<html lang="en">
<head>
<meta charset="utf-8">
<title>Ridgeline Valley Community Trust – Folder Cover</title>
<link href="https://fonts.googleapis.com/css2?family=Roboto+Condensed:wght@400;700&display=swap" rel="stylesheet">
<style>
  :root {
    --green-deep: #125c36;
    --green-bright: #338c48;
    --gold: #eba83a;
    --navy: #2e3079;
    --paper: #fffffe;
  }
  html, body {
    margin: 0;
    padding: 0;
    overflow: hidden;
    background: var(--paper);
  }
  .folder-cover {
    position: relative;
    width: 1200px;
    height: 813px;
    overflow: hidden;
    background: var(--paper);
    font-family: "Roboto Condensed", "Arial Narrow", sans-serif;
  }
  .cover-graphic {
    position: absolute;
    inset: 0;
    width: 100%;
    height: 100%;
  }
  .anniversary-mark {
    position: absolute;
    left: 700px;
    top: 112px;
    width: 140px;
    color: var(--paper);
    font-weight: 700;
    text-align: center;
    line-height: 1;
  }
  .anniversary-mark .years {
    display: block;
    font-size: 40px;
  }
  .anniversary-mark .span {
    display: block;
    margin-top: 6px;
    font-size: 15px;
    letter-spacing: 1px;
  }
  .brand-lockup {
    position: absolute;
    left: 796px;
    top: 696px;
    display: flex;
    align-items: center;
    gap: 10px;
  }
  .brand-square {
    width: 53px;
    height: 44px;
    background: var(--navy);
    flex: none;
  }
  .brand-name {
    margin: 0;
    color: var(--navy);
    font-weight: 700;
    font-size: 23px;
    line-height: 1;
    text-transform: uppercase;
    letter-spacing: -0.2px;
  }
</style>
</head>
<body>
<main class="folder-cover">
  <svg class="cover-graphic" viewBox="10 10 1318 886" preserveAspectRatio="none" aria-hidden="true">
    <defs>
      <linearGradient id="field-green" x1="0" y1="0" x2="1" y2="0">
        <stop offset="0" stop-color="var(--green-deep)"/>
        <stop offset="1" stop-color="var(--green-bright)"/>
      </linearGradient>
    </defs>
    <polygon class="field-green" fill="url(#field-green)" points="10,10 1138,10 606,896 268,896 10,405"/>
    <polygon class="band-gold" fill="var(--gold)" points="1138,10 1246,10 734,896 606,896"/>
    <polygon class="band-gold" fill="var(--gold)" points="10,405 268,896 148,896 10,645"/>
    <polygon class="corner-navy" fill="var(--navy)" points="10,645 148,896 10,896"/>
  </svg>

  <div class="anniversary-mark">
    <span class="years">50 Years</span>
    <span class="span">1969–2019</span>
  </div>

  <div class="brand-lockup">
    <span class="brand-square"></span>
    <p class="brand-name">Ridgeline Valley<br>Community Trust</p>
  </div>
</main>
</body>
</html>
```